The Wagon Rolls Yonder is a food truck, talent show, fundraiser event.

The Pellridge Uplift Foundation is hosting a food truck, talent show, fundraiser called The Wagon Rolls Yonder. We need a flyer designed that incorporates a couple of our existing logos. The theme this year is "Summer Kickoff Jam." The event will be held Wednesday, May 23rd from 3-6 pm at the BRAND NEW Morrow Lakeside Amphitheater (R). I've included some of our logos to incorporate into the flyer. This event is geared towards kids K-12.

Target Market(s)

Kids (K-12) and parents

Industry/Entity Type

Non Profit

Colors

Designer to choose colors to be used in the design.

Requirements
Must have
• Incorporate both logos: Truck (prominent), Foundation logo (not as prominent).
Nice to have
• Might need to have some space to add sponsor logos. Not a must.

```html
<!DOCTYPE html>
<html lang="en">
<head>
<meta charset="utf-8">
<title>Summer Kickoff Jam – The Wagon Rolls Yonder</title>
<link href="https://fonts.googleapis.com/css2?family=Luckiest+Guy&family=Lato:wght@400;700;900&display=swap" rel="stylesheet">
<style>
  :root {
    --stage: #3b3b3b;
    --purple: #5b2a86;
    --purple-deep: #4a1f70;
    --yellow: #f7c21a;
    --sky: #29a8e0;
    --navy: #1f3550;
    --ink: #111111;
    --white: #ffffff;
    --paper: #ffffff;
    --faint: #e4e4e4;
  }
  * { margin: 0; padding: 0; box-sizing: border-box; }
  html, body { width: 1200px; height: 2639px; overflow: hidden; }
  body { background: var(--stage); font-family: "Lato", Arial, sans-serif; }

  .flyer {
    position: absolute; left: 40px; top: 530px;
    width: 1120px; height: 1580px;
    background: var(--paper); overflow: hidden;
  }
  .hero-photo {
    position: absolute; left: 0; top: 0; width: 1120px; height: 440px;
    background: linear-gradient(160deg, #8a6f5a 0%, #c89a86 35%, #5a7fae 65%, #a9b7c9 100%);
  }
  .backdrop { position: absolute; left: 0; top: 0; width: 1120px; height: 1580px; }

  .display { font-family: "Luckiest Guy", "Arial Black", sans-serif; letter-spacing: 2px; line-height: 1; position: absolute; }
  .event-title { left: 52px; top: 448px; font-size: 70px; color: var(--yellow); transform: rotate(-2deg); }
  .weekday { left: 52px; top: 610px; font-size: 50px; color: var(--white); }
  .date { left: 52px; top: 690px; font-size: 84px; color: var(--yellow); }
  .time { left: 52px; top: 900px; font-size: 80px; color: var(--yellow); }
  .time .joiner { display: block; font-size: 38px; color: var(--white); margin: 6px 0 6px 20px; }

  .venue {
    position: absolute; left: 32px; top: 1176px; width: 500px; height: 140px;
    background: var(--sky); transform: skewY(-3deg);
    display: flex; align-items: center; padding: 0 22px 0 20px; gap: 16px;
  }
  .venue > * { transform: skewY(3deg); }
  .venue-pin { width: 30px; height: 40px; flex: none; }
  .venue-text { color: var(--white); font-size: 27px; line-height: 1.2; flex: 1; }
  .venue-name { color: var(--white); font-weight: 700; font-size: 20px; line-height: 1.1; width: 110px; text-align: center; }

  .event-badge {
    position: absolute; left: 438px; top: 586px; width: 680px; height: 680px;
    border-radius: 50%; background: var(--yellow);
    display: flex; align-items: center; justify-content: center; text-align: center;
  }
  .event-badge-name { font-family: "Luckiest Guy", "Arial Black", sans-serif; color: var(--navy); font-size: 78px; line-height: 1.1; letter-spacing: 3px; }

  .presenter { position: absolute; right: 34px; top: 1356px; text-align: right; }
  .presenter-label { font-weight: 900; font-size: 28px; color: var(--ink); }
  .presenter-name { margin-top: 26px; display: flex; align-items: center; justify-content: flex-end; gap: 12px; }
  .presenter-mark { width: 34px; height: 34px; border-radius: 50%; background: var(--navy); flex: none; }
  .presenter-text { font-weight: 900; font-size: 26px; line-height: 1.1; color: var(--navy); width: 200px; text-align: right; }

  .sponsor-row { position: absolute; left: 80px; top: 1456px; display: flex; gap: 62px; }
  .sponsor-slot { width: 70px; height: 70px; border-radius: 50%; background: var(--faint); }
</style>
</head>
<body>
  <main class="flyer">
    <div class="hero-photo" role="img" aria-label="Smiling children with backpacks running out of school together"></div>

    <svg class="backdrop" viewBox="0 0 1120 1580" aria-hidden="true">
      <path d="M0,372 C180,330 330,390 520,376 S880,340 1120,372 L1120,396 C880,370 700,404 520,400 S180,360 0,396 Z" fill="var(--yellow)"/>
      <path d="M0,404 C200,360 360,430 560,414 S900,360 1120,396 L1120,424 C900,392 720,440 560,440 S200,392 0,430 Z" fill="var(--sky)"/>
      <path d="M0,426 C200,388 360,452 560,436 S900,388 1120,420 L1120,1318 C860,1290 560,1330 300,1318 S80,1300 0,1310 Z" fill="var(--purple)"/>
      <path d="M0,1310 C80,1300 300,1318 560,1330 S860,1290 1120,1318 L1120,1342 C860,1316 560,1356 300,1344 S80,1326 0,1336 Z" fill="var(--sky)"/>
      <path d="M0,1336 C80,1326 300,1344 560,1356 S860,1316 1120,1342 L1120,1352 C860,1328 560,1366 300,1354 S80,1338 0,1348 Z" fill="var(--ink)"/>
    </svg>

    <h1 class="display event-title">Summer Kickoff Jam</h1>
    <p class="display weekday">Wednesday</p>
    <p class="display date">May<br>23rd</p>
    <p class="display time">3PM<span class="joiner">to</span>6 PM</p>

    <div class="venue">
      <svg class="venue-pin" viewBox="0 0 30 40" aria-hidden="true">
        <path d="M15,2 C7,2 2,8 2,15 C2,25 15,38 15,38 C15,38 28,25 28,15 C28,8 23,2 15,2 Z" fill="none" stroke="var(--white)" stroke-width="3"/>
        <circle cx="15" cy="15" r="5" fill="var(--white)"/>
      </svg>
      <p class="venue-text">at the Morrow Lakeside Amphitheater<sup>®</sup> at Pellridge Central Park</p>
      <p class="venue-name">Morrow Lakeside</p>
    </div>

    <div class="event-badge">
      <p class="event-badge-name">The Wagon<br>Rolls<br>Yonder</p>
    </div>

    <div class="sponsor-row" aria-label="Sponsor spaces">
      <span class="sponsor-slot"></span><span class="sponsor-slot"></span><span class="sponsor-slot"></span>
      <span class="sponsor-slot"></span><span class="sponsor-slot"></span><span class="sponsor-slot"></span>
    </div>

    <div class="presenter">
      <p class="presenter-label">Presented by</p>
      <div class="presenter-name">
        <span class="presenter-mark"></span>
        <p class="presenter-text">Pellridge Uplift Foundation</p>
      </div>
    </div>
  </main>
</body>
</html>
```